Update the look of Estate Planning booklet to a classic. timeless, professional look

We need a new updated design to our educational Estate Planning booklet. Basic Information will be the same, just need a new look/design throughout the booklet. I've uploaded our new logo, pictures, etc. I would like all pages to have a classic. timeless, professional look.
We are an estate planning law firm that offers Family Estate Planning, Trusts, Wills, Powers of Attorney, Business Succession Planning, Probate & Trust Administration, Asset Protection Planning, Special Needs Planning.
We will be giving this booklet to everyone of our clients. We want to communicate to our clients that we care about you and your families future.
Target Market(s)
Our target market clients in Kansas/Missouri 55+ years old. Generations
Industry/Entity Type
Law Firm
Font styles to use
Requirements
Must have
- Would like the colors to complement our logo colors.
RED - C5 / M100 / Y100 / B25
GOLD - C20 / M50 / Y100 / B42
BLACK - C100 / M100 / Y100 / B100
I also had a black gradient overlay on top of the "R" in the logo.
GRADIENT - white to black(c100 / m100 / y100 / b100)
Page size: Standard letter, 8.5x11 inches
Please add logo on back with -phone number (913) 555-0147 and www.thornwellfirmkc.com
Large R on the back page
19 pages + front and back cover
Nice to have
- We want this document to have a very clean, classy, impressive, professional look to it.

```html
<!DOCTYPE html>
<html lang="en">
<head>
<meta charset="utf-8">
<title>Understanding Estate Planning &amp; Living Trusts — Spread</title>
<link href="https://fonts.googleapis.com/css2?family=Cinzel:wght@400;600&family=Cormorant+Garamond:ital,wght@0,500;1,500&family=Questrial&family=Open+Sans:wght@400;700&display=swap" rel="stylesheet">
<style>
  :root {
    --backdrop: #e4e4e4;
    --paper: #f7f7f7;
    --paper-shade: #ececec;
    --brand-red: #a3161b;
    --brand-gold: #94742c;
    --ink: #2b2b2b;
    --ink-soft: #555;
    --rule: #8a8a8a;
  }
  * { box-sizing: border-box; margin: 0; padding: 0; }
  html, body { width: 1200px; height: 804px; overflow: hidden; }
  body { background: var(--backdrop); font-family: "Open Sans", sans-serif; color: var(--ink); }

  .spread {
    position: absolute; left: 60px; top: 92px;
    width: 1080px; height: 620px;
    display: flex;
    box-shadow: 0 12px 30px rgba(0,0,0,.18);
  }
  .page { position: relative; width: 540px; height: 620px; background: var(--paper); overflow: hidden; }
  .page--left { background: linear-gradient(90deg, var(--paper) 80%, var(--paper-shade)); }
  .page--right { background: linear-gradient(270deg, var(--paper) 85%, var(--paper-shade)); }

  .pattern-fill { position: absolute; }
  .page--left .pattern-fill {
    left: 0; bottom: 0; width: 100%; height: 230px;
    background: linear-gradient(180deg, rgba(220,220,220,0) 0%, #dedede 100%);
  }
  .page--right .pattern-fill {
    right: 0; top: 0; width: 260px; height: 120px;
    background: linear-gradient(200deg, #dcdcdc 0%, rgba(230,230,230,0) 100%);
  }

  .section-title {
    font-family: "Cinzel", serif; font-weight: 600; color: var(--brand-gold);
    letter-spacing: .04em;
  }
  .toc-title { position: absolute; left: 56px; top: 110px; font-size: 20px; }
  .toc-list {
    position: absolute; left: 84px; top: 150px; list-style: none;
    font-family: "Questrial", sans-serif; font-size: 19px; line-height: 1.55; color: var(--ink);
  }
  .toc-list .caps { text-transform: uppercase; }

  .intro {
    position: absolute; left: 56px; top: 410px; width: 430px;
    font-family: "Cormorant Garamond", serif; font-style: italic; font-weight: 500;
    font-size: 14px; line-height: 1.3; color: var(--brand-red);
  }

  .folio {
    position: absolute; bottom: 28px; display: flex; align-items: center; gap: 8px;
    font-family: "Cormorant Garamond", serif; font-size: 11px; color: var(--brand-gold);
  }
  .folio--left { left: 40px; }
  .folio--right { right: 40px; }
  .folio__number { font-size: 12px; color: var(--ink); padding: 0 8px; border-right: 1px solid var(--rule); }
  .folio--right .folio__number { border-right: 0; border-left: 1px solid var(--rule); }
  .folio__firm { font-family: "Cinzel", serif; font-weight: 600; font-size: 12px; color: var(--brand-red); }
  .folio__title .caps { text-transform: uppercase; letter-spacing: .04em; }

  .cases-title { position: absolute; right: 44px; top: 52px; font-size: 17px; }
  .cases {
    position: absolute; left: 44px; top: 92px; width: 452px;
    font-size: 8.6px; line-height: 1.45; color: var(--ink-soft);
  }
  .case { margin-bottom: 11px; text-align: justify; }
  .case__lead { font-weight: 700; color: var(--brand-red); }
</style>
</head>
<body>
  <main class="spread">
    <section class="page page--left">
      <div class="pattern-fill" role="img" aria-label="Faint grey triangular geometric pattern"></div>
      <h2 class="section-title toc-title">Table Of Contents</h2>
      <ol class="toc-list">
        <li>Losing Control with a <span class="caps">Will</span></li>
        <li>Losing Control by <span class="caps">Doing Nothing</span></li>
        <li>Losing Control with <span class="caps">Joint Ownership</span></li>
        <li>Losing Control by <span class="caps">Giving Away Assets</span></li>
        <li>Losing Control with <span class="caps">Beneficiary Designations</span></li>
        <li>Keeping Control with a <span class="caps">Revocable Living Trust</span></li>
      </ol>
      <p class="intro">Taking the time to read this booklet may well be one of the wisest investments you make for yourself and your family. Our intention in writing it is to give you an accurate introduction and general overview of estate planning and living trusts. While there will probably be some variations in your state's laws and terminology, generally these will only be technical and will not effect the overall message.</p>
      <footer class="folio folio--left">
        <span class="folio__number">1</span>
        <span class="folio__firm">Thornwell</span>
        <span class="folio__title">Understanding <span class="caps">Estate Planning</span> &amp; <span class="caps">Living Trusts</span></span>
      </footer>
    </section>

    <section class="page page--right">
      <div class="pattern-fill" role="img" aria-label="Faint grey triangular geometric pattern"></div>
      <h2 class="section-title cases-title">GOOD PLANS CAN GO WRONG</h2>
      <div class="cases">
        <p class="case"><span class="case__lead">To avoid probate after she died, Edith, an elderly widow, decided to give her home to her daughter Susan.</span> They had always gotten along well, and Susan assured her mother she would always have a place to live. Two years later Susan was killed in an accident, and her share of the home passed to her husband, who soon remarried and asked Edith to move out.</p>
        <p class="case"><span class="case__lead">Over the years, John and his wife Eleanor had planned carefully, saved and invested wisely for their retirement.</span> They owned everything jointly and had simple wills leaving all to each other. When John suffered a stroke, Eleanor could not sell their home or manage their accounts without going to court, and a judge was appointed to oversee every decision until his death.</p>
        <p class="case"><span class="case__lead">Claire was lonely after Fred, her husband of 40 years, died.</span> She met a charming younger man at her dance class and soon added his name to her home and savings. When she passed away, he became the sole owner, and her children from her first marriage were left with nothing.</p>
        <p class="case"><span class="case__lead">When George and Betty moved to Florida, they gave their home in New York to their daughter Anne, a divorced mother of three.</span> Anne later remarried, and when she died suddenly the house went to her new husband. George and Betty had no say, and their grandchildren lost the home they had been promised.</p>
        <p class="case"><span class="case__lead">When Edward and Beth married, they both had children and assets from previous marriages.</span> They signed new wills leaving everything to each other, trusting the survivor to divide it fairly. After Edward died, Beth changed her will, and his children were disinherited. The family farm he had built for sixty years had to be sold to pay court costs.</p>
      </div>
      <footer class="folio folio--right">
        <span class="folio__firm">Thornwell</span>
        <span class="folio__title">Understanding <span class="caps">Estate Planning</span> &amp; <span class="caps">Living Trusts</span></span>
        <span class="folio__number">2</span>
      </footer>
    </section>
  </main>
</body>
</html>
```